Update cover page from corporate ppt template

We would like you to design a new cover page for our corporate presentation template

Attached you will find our existing template with the previous cover pages used in the past years.

As you can see, we have used transparency lines in different directions and also tried to develop a new design with mosaic/squares but we are not entirely satisfied (logo lost in the sky, ...)

You can reuse the same picture (mountain with the bridge, i.e not the one of the last cover page)

Feel free to come up with new ideas

```html
<!DOCTYPE html>
<html lang="en">
<head>
<meta charset="utf-8">
<title>Veranta – Board of Directors – May 2024</title>
<link rel="stylesheet" href="https://fonts.googleapis.com/css2?family=Oswald:wght@500&family=Roboto:wght@300;400&display=swap">
<style>
  :root {
    --sky-light: #cfe0f7;
    --sky: #a8c6ef;
    --sky-deep: #8fb4ea;
    --rock: #9aa3b3;
    --autumn: #e4a526;
    --water: #8eaee0;
    --white: #ffffff;
    --brand-grey: #7b7b7b;
    --title-blue: #6a8fd2;
    --ink: #2a2a2a;
  }
  html, body {
    margin: 0;
    padding: 0;
    overflow: hidden;
    background: var(--white);
  }
  .cover {
    position: relative;
    width: 1200px;
    height: 686px;
    overflow: hidden;
    background: var(--white);
    font-family: "Roboto", Arial, sans-serif;
  }
  .cover__art {
    position: absolute;
    inset: 0;
    width: 1200px;
    height: 686px;
  }
  .brand-name {
    position: absolute;
    left: 64px;
    top: 238px;
    margin: 0;
    font-family: "Roboto", Arial, sans-serif;
    font-weight: 300;
    font-size: 96px;
    line-height: 1;
    letter-spacing: 2px;
    color: var(--brand-grey);
  }
  .cover__title {
    position: absolute;
    left: 64px;
    top: 416px;
    margin: 0;
    font-family: "Oswald", Arial, sans-serif;
    font-weight: 500;
    font-size: 46px;
    line-height: 1;
    color: var(--title-blue);
    letter-spacing: 0.4px;
  }
  .cover__date {
    position: absolute;
    left: 64px;
    top: 499px;
    margin: 0;
    font-weight: 400;
    font-size: 28px;
    line-height: 1;
    color: var(--ink);
  }
  .cover__ref {
    position: absolute;
    right: 12px;
    bottom: 8px;
    margin: 0;
    font-size: 11px;
    color: var(--ink);
  }
</style>
</head>
<body>
<main class="cover">
  <svg class="cover__art" viewBox="0 0 1200 686" xmlns="http://www.w3.org/2000/svg">
    <defs>
      <linearGradient id="sceneTones" x1="0" y1="0" x2="0" y2="1">
        <stop offset="0" stop-color="var(--sky-light)"/>
        <stop offset="0.28" stop-color="var(--sky)"/>
        <stop offset="0.45" stop-color="var(--rock)"/>
        <stop offset="0.6" stop-color="var(--autumn)"/>
        <stop offset="0.74" stop-color="var(--autumn)"/>
        <stop offset="0.84" stop-color="var(--water)"/>
        <stop offset="1" stop-color="var(--sky)"/>
      </linearGradient>
      <linearGradient id="skyBand" x1="0" y1="0" x2="1" y2="1">
        <stop offset="0" stop-color="var(--sky-deep)"/>
        <stop offset="1" stop-color="var(--sky-light)"/>
      </linearGradient>
    </defs>

    <rect class="scene" x="0" y="0" width="1200" height="686" fill="url(#sceneTones)"
          role="img" aria-label="Photograph of rocky mountain peaks above a line of golden autumn aspens, mirrored in a calm lake under a clear blue sky"/>

    <path class="scene-veil"
          d="M0 140 L0 686 L530 686 C600 640 640 600 645 520 C650 440 640 390 660 320 C675 255 690 175 700 150 L700 0 L0 0 Z"
          fill="var(--white)" fill-opacity="0.78"/>

    <path class="top-wave"
          d="M0 0 L1200 0 L1200 160 C1150 162 1060 150 990 128 C930 110 860 100 800 130 C760 150 720 180 700 210 C690 190 650 140 560 118 C470 100 300 90 180 100 C100 106 40 125 0 140 Z"
          fill="var(--white)"/>

    <path class="sky-band"
          d="M0 0 L600 0 C580 40 540 70 470 88 C390 106 260 98 170 100 C90 104 35 125 0 150 Z"
          fill="url(#skyBand)"/>
  </svg>

  <p class="brand-name">VERANTA</p>

  <h1 class="cover__title">BOARD OF DIRECTORS</h1>
  <p class="cover__date">MAY 2024</p>
  <p class="cover__ref">C51</p>
</main>
</body>
</html>
```